Label for LiPo Battery Product for RC Hobby Industry

We need your creativity for a new lithium battery label design. We aim to make our product visually appealing and distinct from competitors. Your design skills are crucial for this task, and we're excited to work with you.
Our main label feature is the colour tag profile, designed to easily identify battery category and power level with a 2-way colour band. Inspired by a tool company that uses a consistent colour profile to identify Phillips head sizing across their range.
The design should be modern, clear, convey speed and suitable for both professional and consumer markets.
Target Market(s)
RC, Drone, Camera community. 20-30 year old.
Industry/Entity Type
Battery, Drone Industry, RC Car
Requirements
Must have
- 2-Way colour tag identity profiling, clear text at 100% scale
Nice to have
- Text and graphic alignment. Comfortable padding and formatting. Colour tag profile, clear text."
Should not have
- Basic, stock looking image.

```html
<!DOCTYPE html>
<html lang="en">
<head>
<meta charset="utf-8">
<title>T6420 LiPo Battery Label</title>
<link rel="stylesheet" href="https://fonts.googleapis.com/css2?family=Audiowide&family=Russo+One&family=Lato:wght@400&display=swap">
<style>
  :root {
    --page: #ffffff;
    --label-black: #000000;
    --tag-red: #b71f33;
    --tag-teal: #20a3b3;
    --hot-pink: #ec1759;
    --tread-dark: #2a0612;
    --band-yellow: #fbb016;
    --ink-white: #ffffff;
    --ink-black: #111111;
  }
  html, body {
    margin: 0;
    padding: 0;
    width: 882px;
    height: 1200px;
    overflow: hidden;
    background: var(--page);
  }
  .canvas {
    position: relative;
    width: 882px;
    height: 1200px;
  }
  .battery-label {
    position: absolute;
    left: 95px;
    top: 413px;
    width: 694px;
    height: 373px;
    display: block;
  }
  .product-name {
    font-family: "Russo One", sans-serif;
    font-size: 84px;
    fill: var(--ink-white);
    letter-spacing: 2px;
  }
  .capacity {
    font-family: "Audiowide", sans-serif;
    font-size: 56px;
    fill: var(--ink-white);
  }
  .discharge-rate {
    font-family: "Audiowide", sans-serif;
    font-size: 30px;
    font-style: italic;
    fill: url(#silver);
  }
  .spec {
    font-family: "Audiowide", sans-serif;
    font-size: 25px;
    fill: var(--ink-black);
  }
  .brand-name {
    font-family: "Audiowide", sans-serif;
    font-size: 25px;
    fill: var(--ink-white);
    letter-spacing: 1px;
  }
  .feature {
    font-family: "Lato", sans-serif;
    font-size: 22px;
    fill: var(--ink-black);
  }
</style>
</head>
<body>
<main class="canvas">
  <svg class="battery-label" viewBox="0 0 694 373" xmlns="http://www.w3.org/2000/svg" aria-label="T6420 1300mAh 120C battery label">
    <defs>
      <linearGradient id="silver" x1="0" y1="0" x2="0" y2="1">
        <stop offset="0" stop-color="#ffffff"/>
        <stop offset="0.55" stop-color="#bdbdbd"/>
        <stop offset="1" stop-color="#f2f2f2"/>
      </linearGradient>
      <linearGradient id="swoosh" x1="0" y1="0" x2="1" y2="0">
        <stop offset="0" stop-color="#ec1759" stop-opacity="0.55"/>
        <stop offset="0.6" stop-color="#ec1759" stop-opacity="0.3"/>
        <stop offset="1" stop-color="#ec1759" stop-opacity="0"/>
      </linearGradient>
      <linearGradient id="tread" x1="0" y1="1" x2="1" y2="0">
        <stop offset="0" stop-color="#3a0818"/>
        <stop offset="1" stop-color="#14030a"/>
      </linearGradient>
    </defs>

    <rect class="label-base" x="0" y="0" width="694" height="373" fill="var(--label-black)"/>

    <path class="speed-swoosh" role="img" aria-label="Flowing speed-line graphic"
          d="M33 260 C150 240 300 250 420 180 C480 150 520 130 560 125 C470 170 420 230 300 305 C200 320 100 330 33 330 Z"
          fill="url(#swoosh)"/>

    <polygon class="pink-panel" points="541,0 694,0 694,373 319,373" fill="var(--hot-pink)"/>

    <polygon class="tire-tread" role="img" aria-label="Distressed tyre tread track graphic"
             points="600,0 694,0 694,60 519,373 407,373" fill="url(#tread)"/>

    <rect class="colour-tag colour-tag--red" x="0" y="0" width="16" height="373" fill="var(--tag-red)"/>
    <rect class="colour-tag colour-tag--teal" x="16" y="0" width="17" height="373" fill="var(--tag-teal)"/>

    <text class="product-name" x="52" y="117" textLength="404" lengthAdjust="spacingAndGlyphs">T6420</text>

    <text class="capacity" x="54" y="180" textLength="316" lengthAdjust="spacingAndGlyphs">1300mAh</text>
    <text class="discharge-rate" x="385" y="177" textLength="115" lengthAdjust="spacingAndGlyphs">120C</text>

    <polygon class="spec-band" points="65,198 514,198 494,234 45,234" fill="var(--band-yellow)"/>
    <text class="spec" x="87" y="226" textLength="93" lengthAdjust="spacingAndGlyphs">22.2V</text>
    <text class="spec" x="220" y="226" textLength="79" lengthAdjust="spacingAndGlyphs">1.3Ah</text>
    <text class="spec" x="337" y="226" textLength="137" lengthAdjust="spacingAndGlyphs">6 CELLS</text>

    <text class="brand-name" transform="translate(676 158) rotate(-90)" textLength="136" lengthAdjust="spacingAndGlyphs">VOLTARO</text>

    <rect class="feature-strip" x="33" y="316" width="661" height="33" fill="var(--ink-white)"/>
    <text class="feature" x="54" y="341">Performance</text>
    <text class="feature" x="199" y="341">|</text>
    <text class="feature" x="228" y="341">Armour Protection</text>
    <text class="feature" x="437" y="341">|</text>
    <text class="feature" x="466" y="341">Advanced Insulation</text>
  </svg>
</main>
</body>
</html>
```